we are an outdoor outlet in a country club that has a variety of outlets. The Club is called Brookhaven and is located in Cairo, Egypt. This garden menu will include cuisines from the Mediterranean, Asia and Texmex. we need a menu that is colorful and would fit an A3 size, back and front are to be used. Attached is the old menu currently in use (Garden Menu 2012.pdf is just for reference) and the new menu text for you to use is under the name Garden Menu Fall 2013
thank you.

```html
<!DOCTYPE html>
<html lang="en">
<head>
<meta charset="utf-8">
<title>Brookhaven Garden Menu – Front and Back</title>
<link rel="stylesheet" href="https://fonts.googleapis.com/css2?family=Archivo:wght@400;700;800&family=Questrial&display=swap">
<style>
  :root{
    --backdrop:#b4b4b4;
    --paper:#ffffff;
    --cream:#fdeb8e;
    --orange:#dc5a1e;
    --lime:#b6cc1d;
    --ink:#3e1c0e;
    --brand:#5b2a15;
  }
  *{margin:0;padding:0;box-sizing:border-box}
  html,body{width:1200px;height:707px;overflow:hidden}
  body{background:var(--backdrop);font-family:"Archivo",Arial,sans-serif;color:var(--ink);position:relative}
  .side-label{position:absolute;top:66px;font-family:"Questrial",sans-serif;font-size:31px;color:#fff}
  .side-label--front{left:35px}
  .side-label--back{left:1102px}
  .menu-page{position:absolute;top:68px;width:380px;height:568px;background:var(--cream);overflow:hidden;box-shadow:0 3px 8px rgba(0,0,0,.35)}
  .menu-page--front{left:118px}
  .menu-page--back{left:686px}
  .shapes{position:absolute;left:0;top:0;z-index:0}
  .shape-orange{fill:var(--orange)}
  .shape-cream{fill:var(--cream)}
  .page-header{position:absolute;left:0;top:0;width:380px;height:113px;background:var(--paper);z-index:1}
  .menu-tab{position:absolute;left:12px;top:2px;width:30px;height:104px;background:var(--orange);display:flex;align-items:flex-start;justify-content:center}
  .menu-tab span{writing-mode:vertical-rl;color:#fff;font-weight:800;font-size:15px;letter-spacing:1px;margin-top:20px}
  .brand{position:absolute;left:100px;width:180px;top:22px;text-align:center}
  .brand-dot{display:block;width:26px;height:26px;border-radius:50%;background:var(--lime);margin:0 auto 8px}
  .brand-name{font-family:"Questrial",sans-serif;font-size:25px;color:var(--brand);line-height:1;text-transform:lowercase}
  .section-label{position:absolute;z-index:2;background:var(--lime);color:#fff;font-weight:700;font-size:9px;text-align:center;display:flex;align-items:center;justify-content:center;clip-path:polygon(0 8%,100% 0,99% 92%,1% 100%)}
  .menu-block{position:absolute;z-index:2;text-align:center;font-size:4.4px;line-height:5.6px}
  .menu-block h3{font-size:8px;font-weight:800;line-height:11px;margin-bottom:1px}
  .menu-block h4{font-size:4.6px;font-weight:700;line-height:5.6px}
</style>
</head>
<body>

<div class="side-label side-label--front">front</div>
<div class="side-label side-label--back">back</div>

<section class="menu-page menu-page--front">
  <svg class="shapes" width="380" height="568" viewBox="0 0 380 568">
    <polygon class="shape-orange" points="18,130 376,116 375,515 100,522 96,452 20,452"/>
    <polygon class="shape-cream" points="27,142 192,136 194,206 29,209"/>
    <polygon class="shape-cream" points="22,222 212,216 208,299 24,302"/>
    <polygon class="shape-cream" points="212,140 382,126 382,258 220,264"/>
    <polygon class="shape-cream" points="237,274 372,270 374,306 241,308"/>
    <polygon class="shape-cream" points="52,312 152,313 154,337 55,336"/>
    <polygon class="shape-cream" points="247,320 366,315 369,367 250,370"/>
    <polygon class="shape-cream" points="32,343 182,337 180,392 36,394"/>
    <polygon class="shape-cream" points="100,404 348,400 352,518 104,522"/>
  </svg>
  <header class="page-header">
    <div class="menu-tab"><span>MENU</span></div>
    <div class="brand"><span class="brand-dot"></span><div class="brand-name">Brookhaven</div></div>
  </header>
  <div class="section-label" style="left:144px;top:110px;width:126px;height:20px">Mediterranean Corner</div>

  <div class="menu-block" style="left:30px;top:147px;width:162px">
    <h3>Soups:</h3>
    <p>Tomato Basil</p><p>Simmered tomato soup finished with fresh basil and cream</p>
    <p>Chicken Cream</p><p>Chicken broth with roasted chicken cubes, pine nuts, and cream</p>
    <p>Moroccan Harira</p><p>Vegetable broth with fresh tomato, chickpeas, lentil, cilantro, and diced lamb</p>
  </div>
  <div class="menu-block" style="left:26px;top:227px;width:182px">
    <h3>Salads:</h3>
    <p>Caprese</p><p>Buffalo mozzarella and sliced tomato with a balsamic vinaigrette</p>
    <p>Rocket Apple</p><p>Rocket leaves with gorgonzola, croutons, and strawberry vinaigrette</p>
    <p>French Riviera Nicoise</p><p>Lettuce, egg, tomato, tuna, olives, onion, celery, radish, bell pepper in a French vinaigrette</p>
    <p>Folie</p><p>Mixed greens with crab sticks, mushroom, corn, cherry tomato in a mango vinaigrette</p>
  </div>
  <div class="menu-block" style="left:216px;top:144px;width:162px">
    <h3>Appetizers:</h3>
    <p>Salmon tartare seasoned with lemon juice, garlic, and crushed black pepper</p>
    <p>Roasted eggplant rolls with herbed ricotta cheese and pine nuts</p>
    <p>Falafel in mini pita served with tehina and oriental salsa</p>
    <p>Manaousha with thyme and olive oil</p>
    <p>Fried kobeba with minced meat, spices, and pine nuts</p>
    <p>Fried calamari a la Romana served with aioli</p>
    <p>Sambousek with herbed white cheese and mint</p>
    <p>Oriental sausage sautéed with garlic and onion</p>
    <p>Mini vine leaves with a yoghurt dip</p>
    <p>Fatouch with a pomegranate syrup dressing</p>
    <p>Hummus seasoned with lemon juice, garlic, and olive oil</p>
    <p>White cheese with diced tomato, thyme, and olive oil</p>
    <p>Tehina seasoned with cumin, lemon juice, and garlic</p>
  </div>
  <div class="menu-block" style="left:240px;top:274px;width:132px">
    <h3>Pizza &amp; Pasta:</h3>
    <p>Pizza Margarita (Choose your toppings)</p><p>Create your own pasta</p><p>Type: Spaghetti, Tagliatelle, Penne</p>
  </div>
  <div class="menu-block" style="left:55px;top:314px;width:98px">
    <h3>Sauces:</h3><p>Napolitana, Bolognese, Alfredo</p>
  </div>
  <div class="menu-block" style="left:250px;top:322px;width:116px">
    <h3>Toppings:</h3>
    <p>Bell peppers, olives, tomato, onion</p><p>Mushroom, chicken, tuna, pepperoni</p><p>Smoked salmon, shrimps</p><p>Lasagna</p>
  </div>
  <div class="menu-block" style="left:36px;top:343px;width:144px">
    <h3>Sandwiches:</h3>
    <p>(Served with French fries or a garden salad)</p><p>Beef or chicken Shawerma</p><p>Grilled kofta</p>
    <p>Greek lamb gyro in pita bread with Tzatziki</p><p>Club sandwich with smoked beef, turkey, egg</p>
  </div>
  <div class="menu-block" style="left:104px;top:410px;width:244px">
    <h3>Main Courses:</h3>
    <p>Veal Parmeggiana</p><p>Breaded veal escalope topped with melted cheese and tomato sauce served with Spaghetti</p>
    <p>Chicken a la Francaise</p><p>Pan fried chicken breast in a mushroom cream sauce with vegetables white rice</p>
    <p>Grilled Salmon</p><p>Salmon steak charcoal grilled with avocado tomato relish and creamy mushroom risotto</p>
    <p>Moroccan Chicken</p><p>Chicken cubes simmered with spices and olives served with tomato rice</p>
    <p>Filet</p><p>Tender filet grilled to your liking served with mashed potato and creamed spinach</p>
    <p>Choice of sauces: Brown mushroom, Green Peppercorn, Gorgonzola</p>
  </div>
</section>

<section class="menu-page menu-page--back">
  <svg class="shapes" width="380" height="568" viewBox="0 0 380 568">
    <polygon class="shape-orange" points="12,124 376,116 374,160 10,158"/>
    <polygon class="shape-orange" points="225,182 378,180 378,196 228,198"/>
    <polygon class="shape-orange" points="16,244 372,240 370,290 18,294"/>
    <polygon class="shape-cream" points="8,150 200,146 202,236 10,242"/>
    <polygon class="shape-cream" points="214,140 374,136 372,178 216,180"/>
    <polygon class="shape-cream" points="218,202 378,198 376,276 222,272"/>
    <polygon class="shape-orange" points="24,302 374,298 372,437 26,433"/>
    <polygon class="shape-cream" points="82,316 354,310 350,428 86,430"/>
    <polygon class="shape-orange" points="22,450 379,446 378,546 24,548"/>
    <polygon class="shape-cream" points="104,462 322,458 324,544 110,546"/>
  </svg>
  <header class="page-header">
    <div class="menu-tab"><span>MENU</span></div>
    <div class="brand"><span class="brand-dot"></span><div class="brand-name">Brookhaven</div></div>
  </header>
  <div class="section-label" style="left:162px;top:102px;width:80px;height:22px">Asian Corner</div>
  <div class="section-label" style="left:176px;top:284px;width:56px;height:28px">Tex Mex</div>
  <div class="section-label" style="left:176px;top:432px;width:68px;height:22px">Desserts</div>

  <div class="menu-block" style="left:12px;top:156px;width:186px">
    <h3>Salads &amp; Appetizers:</h3>
    <p>Chicken Wasabi Salad</p><p>Diced chicken with a mayo wasabi dressing on top of shredded lettuce</p>
    <p>Chicken Sesame Noodle Salad</p><p>Sesame crusted chicken with glass noodles tossed with sweet chili, soy sauce, and lemongrass</p>
    <p>Spring rolls</p><p>Vegetable spring rolls served with house made sweet and sour dip</p>
    <p>Indian Samosa</p><p>Fried dough parcels filled with vegetables and spices</p>
  </div>
  <div class="menu-block" style="left:218px;top:144px;width:152px">
    <h3>Main Courses:</h3>
    <p>Murgh Chicken Makhni</p><p>Chicken cubes in a rich creamy tomato sauce seasoned with garam masala</p>
  </div>
  <div class="menu-block" style="left:222px;top:206px;width:152px">
    <h3>Choice of side:</h3>
    <p>vegetable korma or curd</p><p>Chicken Tandoori</p>
    <p>Grilled chicken cubes with tandoori spices served with basmati rice</p>
    <p>Thai Coconut Curry Shrimp</p><p>Sautéed shrimp tossed with curry and coconut milk served with jasmine rice</p>
    <p>Mongolian Beef</p><p>Soy marinated beef with oyster sauce and vegetables served with egg noodles</p>
  </div>
  <div class="menu-block" style="left:86px;top:318px;width:264px">
    <h3>Salads &amp; Appetizers:</h3>
    <p>Caesar Salad</p><p>Iceberg lettuce with Caesar dressing with grated Parmesan cheese and croutons</p>
    <p>Taco salad 42</p><p>Chicken breast, beans, sour cream, guacamole, tomato, corn, lettuce, olives, chives, vinaigrette</p>
    <p>Nachos topped with chili, melted cheese, beans</p><p>Chicken Quesadilla served with guacamole, salsa, and sour cream</p>
    <h4>Main Courses &amp; Sandwiches:</h4>
    <p>Cheeseburger</p><p>House made lean beef burger topped with cheddar cheese</p>
    <p>Mushroom Burger</p><p>Beef burger with sautéed mushroom, caramelized onion, and provolone cheese</p>
    <p>Crispy Chicken Wrap</p><p>Crisp fried chicken wrap with a ranch dressing</p>
    <p>Fajita (Chicken, Beef, Combo)</p><p>Pan seared meat or chicken with onion and bell pepper served with sour cream, guacamole, salsa</p>
  </div>
  <div class="menu-block" style="left:108px;top:464px;width:214px">
    <p>Mix Berries Cheesecake</p><p>Crème Brulee</p><p>Chocolate Caramel Cake</p><p>Warm Chocolate Fondant</p>
    <p>Baked Apple Tart Tatin</p><p>Tiramisu</p><p>Pumpkin Pie Flan</p><p>Mixed Berries Granola Yoghurt</p>
    <p>Vanilla Ice Cream Profiterole with dark and white chocolate sauce</p>
    <p>Caramelized Banana with Deep Fried Ice Cream</p><p>Baklawa with Nuts and Sugar Syrup</p>
    <p>Shot Glass Sampler – Tiramisu, Chocolate Crisp Mousse, Pear with Sabayon</p><p>Ice Cream by Scoop</p>
  </div>
</section>

</body>
</html>
```